依頼詳細
?当社のホームページ
https://meadowpine-kai.com/
https://www.vidoramahub.com/channel/UCrT8bLqZx3mVn0JdKs5FgWe
https://chirplane.com/kaedenoaniki
https://www.snapgallo.com/kaede.morinaga/

?ご依頼詳細
「この中に初めてご来店の方へ」という長方形のバナーがありますが、こちらと同サイズのバナーを製作いただきたいと考えております。バナーは、パソコンとスマホ用でサイズが異なるためお手数ですが、GoogleChromeなどの開発ツールで各サイズについてはご確認ください。

バナーの内容は「アクセスランキング」というホストのプロフィールページの週間アクセス数をランキング化したページを案内するものとなります。アクセスランキングは、ナイトワークなどのポータルサイトなどではよくあるのですが、キャストブログやキャストプロフィールがどのくらい見られているのかをランキング化したものです。こちらもお調べいただくと出てくるかと思います。

当社は、ホストクラブにありがちなギラギラとしたイメージを排し、気さくで親近感のある店鋪作り、SNS発信を心がけております。ホストクラブの怪しい雰囲気は、集客にも求人にも向いていないためです。なので、「黒背景」「蜘蛛や蝶のモチーフ」などはあまり好みません。一見ホストクラブだとは気づかれないような明るくクリーンなバナーデザインを希望いたします。

?継続依頼希望者大歓迎です。
今後も継続的にバナー制作を依頼したいと思っております。業務の都合上、細かなデザインの指定ができませんが、当社の雰囲気やイメージ、ホストという仕事を理解してくださる方で継続依頼、長期の外注契約を希望する方は大歓迎です。
もし、ご興味がある方はその旨をご連絡いただけますと非常に助かります。
記載項目
ロゴは添付ファイルをご確認ください。
このほか、不明点などはご連絡いただけますと助かります。
サイズ
• 当社ホームページをご確認ください。
希望イメージ
シンプル 複雑
単色 カラフル
暗い 明るい
日常 高級
遊び心 厳粛
未来的 伝統的
女性的 男性的
希望する色
納品ファイル
• 高解像度JPG (.jpg)
補足説明
■ 選んだ理由

弊社のホームページをご覧いただいた上で、制作されたことがよくわかりデザインでした。おかげさまでよく馴染むデザインになったように感じます。

■ 提案者全員のお礼・コメント

皆様、お忙しい中ご提案いただきまして本当にありがとうございました。ご提案いただいた作品全て非常にクオリティが高く検討に時間を要してしまいました。今後ともよろしくお願いいたします。

```html
<!DOCTYPE html>
<html lang="ja">
<head>
<meta charset="UTF-8">
<title>Weekly Access Ranking</title>
<link rel="stylesheet" href="https://fonts.googleapis.com/css2?family=Pacifico&family=Cinzel:wght@500&family=Noto+Sans+JP:wght@500&display=swap">
<style>
  :root {
    --bokeh-gold: #e9d39a;
    --bokeh-cream: #f4ead0;
    --bokeh-lilac: #b9b6dc;
    --bokeh-blue: #8f9fd6;
    --bokeh-deep: #6f82c4;
    --title-blue: #6f8fe6;
    --title-purple: #b07de0;
    --title-edge: #ffffff;
    --brand-gold: #c9a447;
    --caption-white: #ffffff;
    --portrait-light: #bdbdbd;
    --portrait-dark: #3a3a3a;
    --ring-gold: #d9b558;
    --star-gold: #f2c33a;
  }
  * { margin: 0; padding: 0; box-sizing: border-box; }
  html, body { width: 1200px; height: 560px; overflow: hidden; }
  .banner {
    position: relative;
    width: 1200px;
    height: 560px;
    overflow: hidden;
  }
  .banner__backdrop {
    position: absolute;
    inset: 0;
    background:
      radial-gradient(ellipse 45% 50% at 20% 15%, var(--bokeh-cream), transparent 70%),
      radial-gradient(ellipse 40% 40% at 85% 20%, var(--bokeh-gold), transparent 70%),
      radial-gradient(ellipse 50% 45% at 15% 90%, var(--bokeh-deep), transparent 75%),
      linear-gradient(170deg, var(--bokeh-gold) 0%, var(--bokeh-lilac) 45%, var(--bokeh-blue) 80%, var(--bokeh-deep) 100%);
  }
  .title {
    position: absolute;
    font-family: "Pacifico", cursive;
    line-height: 1;
    background: linear-gradient(180deg, var(--title-blue) 20%, var(--title-purple) 85%);
    -webkit-background-clip: text;
    background-clip: text;
    color: transparent;
    -webkit-text-stroke: 2px var(--title-edge);
    filter: drop-shadow(0 3px 4px rgba(80, 70, 140, 0.35));
    white-space: nowrap;
  }
  .title--weekly { left: 190px; top: 38px; font-size: 92px; transform: rotate(-6deg); }
  .title--ranking { left: 40px; top: 168px; font-size: 88px; transform: rotate(-6deg); letter-spacing: -2px; }
  .brand {
    position: absolute;
    left: 100px;
    top: 362px;
    display: flex;
    align-items: center;
    gap: 14px;
  }
  .brand__dot {
    width: 44px; height: 44px;
    border-radius: 50%;
    background: var(--brand-gold);
  }
  .brand__name {
    font-family: "Cinzel", serif;
    font-weight: 500;
    font-size: 30px;
    letter-spacing: 1px;
    color: var(--brand-gold);
  }
  .caption {
    position: absolute;
    left: 36px;
    top: 448px;
    font-family: "Noto Sans JP", sans-serif;
    font-weight: 500;
    font-size: 38px;
    letter-spacing: 2px;
    color: var(--caption-white);
    text-shadow: 0 2px 6px rgba(60, 60, 110, 0.45);
  }
  .portrait {
    position: absolute;
    left: 742px;
    top: 40px;
    width: 400px;
    height: 400px;
    border-radius: 50%;
    background: radial-gradient(circle at 40% 35%, var(--portrait-light), #8a8a8a 55%, var(--portrait-dark) 100%);
    box-shadow: 0 0 0 4px var(--ring-gold), 0 6px 18px rgba(60, 50, 100, 0.35);
  }
  .rating {
    position: absolute;
    left: 820px;
    top: 440px;
    width: 260px;
    height: 90px;
  }
</style>
</head>
<body>
  <main class="banner">
    <div class="banner__backdrop" role="img" aria-label="Soft golden and blue bokeh lights background"></div>

    <h1 class="title-group">
      <span class="title title--weekly">Weekly</span>
      <span class="title title--ranking">AccessRanking</span>
    </h1>

    <div class="brand">
      <span class="brand__dot"></span>
      <span class="brand__name">MEADOWPINE GROUP</span>
    </div>

    <p class="caption">週間アクセスランキング</p>

    <div class="portrait" role="img" aria-label="Monochrome photo of a host beside a champagne glass tower, framed by a gold laurel wreath"></div>

    <svg class="rating" viewBox="0 0 260 90" aria-hidden="true">
      <defs>
        <polygon id="star" points="0,-10 2.94,-4.05 9.51,-3.09 4.76,1.55 5.88,8.09 0,5 -5.88,8.09 -4.76,1.55 -9.51,-3.09 -2.94,-4.05"/>
      </defs>
      <g fill="var(--star-gold)" stroke="#fff6d5" stroke-width="0.6">
        <use href="#star" transform="translate(20 68) scale(1.6)"/>
        <use href="#star" transform="translate(64 58) scale(2.4)"/>
        <use href="#star" transform="translate(128 44) scale(3.8)"/>
        <use href="#star" transform="translate(192 58) scale(2.4)"/>
        <use href="#star" transform="translate(236 68) scale(1.6)"/>
      </g>
    </svg>
  </main>
</body>
</html>
```